Banner Ad Design Project

We need a Banner to hang outside our Health Food Store to advertise to the public that we will be holding an Organic Market Day every Saturday.
We have our Business name and logo that will need to be incorporated into the design.
We want the design to convey freshness and have an earthy / farm feel, but also want the design to be crisp and not "Hippie"
we also need the banner to say "Fresh Organic Market every Saturday"
we will be selling fresh organic fruit and vegetables.
Target Market(s)
existing customers and general public walking past the shop
Industry/Entity Type
Farm
Look and feel

```html
<!DOCTYPE html>
<html lang="en">
<head>
<meta charset="utf-8">
<title>Larkfield Wholefoods Store – Saturday Market Banner</title>
<link rel="stylesheet" href="https://fonts.googleapis.com/css2?family=Arimo:wght@700&display=swap">
<style>
  :root {
    --rust: #b0481f;
    --sun: #fff200;
    --paper: #ffffff;
  }
  html, body {
    margin: 0;
    padding: 0;
    width: 1200px;
    height: 900px;
    overflow: hidden;
    background: var(--paper);
  }
  .banner {
    position: relative;
    width: 1200px;
    height: 900px;
    font-family: "Arimo", Arial, sans-serif;
    font-weight: 700;
    background: var(--paper);
  }
  .headline-band {
    position: absolute;
    top: 0;
    left: 0;
    width: 1200px;
    height: 250px;
    background: var(--rust);
    color: var(--sun);
    display: flex;
    flex-direction: column;
    align-items: center;
    justify-content: center;
    text-align: center;
  }
  .headline-line {
    display: block;
    font-size: 90px;
    line-height: 102px;
    letter-spacing: 2px;
  }
  .store-name {
    position: absolute;
    top: 250px;
    left: 0;
    width: 1200px;
    height: 548px;
    display: flex;
    flex-direction: column;
    align-items: center;
    justify-content: center;
    color: var(--rust);
    text-transform: lowercase;
  }
  .store-name-primary {
    display: block;
    font-size: 170px;
    line-height: 180px;
    letter-spacing: 4px;
    align-self: flex-start;
    margin-left: 140px;
  }
  .store-name-secondary {
    display: block;
    font-size: 142px;
    line-height: 170px;
    letter-spacing: 1px;
  }
  .produce-band {
    position: absolute;
    left: 0;
    bottom: 0;
    width: 1200px;
    height: 102px;
    background: var(--rust);
    color: var(--sun);
    display: flex;
    align-items: center;
    justify-content: center;
    font-size: 50px;
    letter-spacing: 2px;
  }
</style>
</head>
<body>
  <main class="banner">
    <header class="headline-band">
      <span class="headline-line">Fresh Organic Market</span>
      <span class="headline-line">Every Saturday</span>
    </header>

    <section class="store-name">
      <span class="store-name-primary">larkfield</span>
      <span class="store-name-secondary">wholefoods store</span>
    </section>

    <footer class="produce-band">Fresh Organic Fruit and Vegetables</footer>
  </main>
</body>
</html>
```